Willowmere Counseling (Endure - Mend - Flourish) - Double Sided Business Card

I would like a 2-sided business card. Front: Matte Black or Navy with Logo & Tagline. Back: Name, Address, Phone Number, Email, & Website (maybe would like to include a small map pin-pointing location); Prefer front to be a gold/silver foil (iridescent); Back prefer white or light colored background with lettering that is easy to read and simple

Target Market(s)

Individuals & Couples (13 y.o. - ALL Adults); High end clientele

Industry/Entity Type

Licensed Professional Counselor (Mental Health)

Contact Information for Business Card

Name: Willowmere Counseling; Tagline: Endure - Mend - Flourish; Address: 3870 N. Garrick Ave., Suite 214, Fort Worth, TX 76132; Phone: (214) 555-0187; Website: www.WillowmereCounseling.example

Font styles to use
Serif

Requirements
Must have
• Logo on Front (Large) prefer gold/silver foil on a matte dark color (i.e. black, navy, etc.); Back of Card: All other relevant information

```html
<!DOCTYPE html>
<html lang="en">
<head>
<meta charset="utf-8">
<title>Willowmere Counseling – Business Card</title>
<link rel="stylesheet" href="https://fonts.googleapis.com/css2?family=Cinzel:wght@500&family=Montserrat:wght@600&family=Roboto:wght@400&display=swap">
<style>
  :root {
    --backdrop: #e6e6e6;
    --gold: #c9ae55;
    --gold-deep: #b89a3e;
    --paper: #f7f7f5;
    --charcoal: #2a2a2a;
    --slate: #6d6e70;
    --ink: #3c3c3c;
  }
  * { box-sizing: border-box; margin: 0; padding: 0; }
  html, body { width: 1200px; height: 884px; overflow: hidden; }
  body {
    background: var(--backdrop);
    display: flex;
    flex-direction: column;
    align-items: center;
    justify-content: center;
    gap: 40px;
  }
  .card {
    width: 560px;
    height: 320px;
    position: relative;
    box-shadow: 0 14px 30px rgba(0,0,0,0.14);
  }

  /* Front */
  .card--front {
    background: var(--gold);
    display: flex;
    align-items: center;
    justify-content: center;
  }
  .brand {
    display: flex;
    flex-direction: column;
    align-items: center;
    gap: 12px;
  }
  .brand__row { display: flex; align-items: center; gap: 14px; }
  .brand__dot {
    width: 34px; height: 34px; border-radius: 50%;
    background: var(--charcoal);
  }
  .brand__name {
    font-family: "Cinzel", serif;
    font-weight: 500;
    font-size: 30px;
    letter-spacing: 2px;
    color: var(--charcoal);
  }
  .brand__tagline {
    display: flex; align-items: center; gap: 12px;
    font-family: "Cinzel", serif;
    font-size: 12px;
    letter-spacing: 1.5px;
    color: var(--charcoal);
  }
  .brand__tagline::before, .brand__tagline::after {
    content: ""; width: 60px; height: 2px; background: var(--charcoal);
  }

  /* Back */
  .card--back { background: var(--paper); }
  .card--back .brand {
    position: absolute; top: 38px; right: 36px; gap: 8px;
  }
  .card--back .brand__name { font-size: 19px; color: var(--slate); letter-spacing: 1.5px; }
  .card--back .brand__dot { width: 22px; height: 22px; background: var(--gold); }
  .card--back .brand__row { gap: 10px; }
  .card--back .brand__tagline { font-size: 8.5px; color: var(--gold-deep); gap: 8px; }
  .card--back .brand__tagline::before, .card--back .brand__tagline::after { width: 34px; height: 1.5px; background: var(--slate); }

  .person { position: absolute; left: 36px; top: 128px; }
  .person__name {
    font-family: "Montserrat", sans-serif;
    font-weight: 600;
    font-size: 15px;
    color: var(--gold);
    text-transform: uppercase;
    letter-spacing: 0.3px;
  }
  .person__role {
    font-family: "Roboto", sans-serif;
    font-size: 13px;
    color: var(--ink);
    margin-top: 3px;
  }
  .divider {
    position: absolute; left: 180px; right: 36px; top: 162px;
    height: 1px; background: var(--ink);
  }
  .contact {
    position: absolute; left: 36px; bottom: 36px;
    list-style: none;
    font-family: "Roboto", sans-serif;
    font-size: 13px;
    color: var(--ink);
    display: flex; flex-direction: column; gap: 4px;
  }
  .contact li { display: flex; align-items: center; gap: 8px; }
  .contact svg { width: 13px; height: 13px; fill: none; stroke: var(--gold); stroke-width: 2; }
  .address {
    position: absolute; right: 36px; bottom: 36px;
    font-family: "Roboto", sans-serif;
    font-style: normal;
    font-size: 13px;
    line-height: 1.45;
    color: var(--ink);
    text-align: right;
  }
</style>
</head>
<body>
  <section class="card card--front" aria-label="Card front">
    <div class="brand">
      <div class="brand__row">
        <span class="brand__dot"></span>
        <span class="brand__name">Willowmere Counseling</span>
      </div>
      <p class="brand__tagline">Endure - Mend - Flourish</p>
    </div>
  </section>

  <section class="card card--back" aria-label="Card back">
    <div class="brand">
      <div class="brand__row">
        <span class="brand__dot"></span>
        <span class="brand__name">Willowmere Counseling</span>
      </div>
      <p class="brand__tagline">Endure - Mend - Flourish</p>
    </div>

    <div class="person">
      <p class="person__name">Delia Harrow, MS, LPC</p>
      <p class="person__role">Managing Director</p>
    </div>
    <div class="divider"></div>

    <ul class="contact">
      <li>
        <svg viewBox="0 0 16 16"><path d="M3 2h3l1.5 3.5-2 1.2a8 8 0 0 0 3.8 3.8l1.2-2L14 10v3a1 1 0 0 1-1 1A11 11 0 0 1 2 3a1 1 0 0 1 1-1z"/></svg>
        (214) 555-0187
      </li>
      <li>
        <svg viewBox="0 0 16 16"><rect x="1.5" y="3.5" width="13" height="9"/><path d="M1.5 3.5 8 9l6.5-5.5"/></svg>
        info@WillowmereCounseling.example
      </li>
      <li>
        <svg viewBox="0 0 16 16"><circle cx="8" cy="8" r="6.5"/><path d="M1.5 8h13M8 1.5c-2.5 3-2.5 10 0 13M8 1.5c2.5 3 2.5 10 0 13"/></svg>
        www.WillowmereCounseling.example
      </li>
    </ul>

    <address class="address">
      3870 N. Garrick Ave.,<br>
      Suite 214,<br>
      Fort Worth, TX 76132
    </address>
  </section>
</body>
</html>
```